Brightwell-Joinery - DL Flyer - Kitchen Renovations & Cabinetry - Eye Catching Design

Please design a creative, professional DL flyer for us (DL Size: 98 x 210mmm), incorporating details outlined below...

Font: Helvetica Neue (same as logo)

Front: Main logo (01.eps) as a feature, website on the bottom (brightwell-joinery.com.au).

Back: Three key words to be featured: Kitchens I Benchtops I Custom Cabinetry
2-3 clear images showing our work (more have been provided so you can select the images that work the best with the design). We have also attached the icon from our logo on 4 x different colour backgrounds, which could be incorporated (on back).
Text to include: 'Servicing all areas, we come to you!'

Contact details: 'Call us now on 0461 872 309'. enquiries@brightwell-joinery.com.au Lic. No. BLD 738402

Look forward to seeing what you come up with.

Target Market(s)

Home owners, 35-80+ age bracket

Industry/Entity Type

Kitchen

Font styles to use
Other font styles liked:
• Helvetica Neue

Requirements
Must have
• Logo and website on front page of flyer. Minimum of 2-3 images incorporated. Contact details as per project description. Text on back page, 3 key words: Kitchens I Benchtops I Custom Cabinetry
• Creative, eye-catching design layout. Consistent theming with business card (see attached), including colours (grey, white, blues)
Nice to have
• Creative, eye-catching way to incorporate photos.
Should not have
• Not too busy/cluttered

```html
<!DOCTYPE html>
<html lang="en">
<head>
<meta charset="utf-8">
<title>Brightwell-Joinery DL Flyer</title>
<link href="https://fonts.googleapis.com/css2?family=Inter:wght@300;400;600;700&display=swap" rel="stylesheet">
<style>
  :root {
    --ink: #4a4f55;
    --ink-soft: #6a7077;
    --blue-deep: #3d8fd0;
    --blue-light: #9ccaea;
    --blue-pale: #eaf4fc;
    --white: #ffffff;
  }
  html, body { margin: 0; padding: 0; overflow: hidden; background: var(--white); }
  .flyer {
    position: relative; width: 1120px; height: 1200px; overflow: hidden;
    font-family: "Inter", "Helvetica Neue", Arial, sans-serif;
  }
  .panel { position: absolute; top: 0; height: 1200px; width: 560px; overflow: hidden; }
  .panel--front { left: 0; background: radial-gradient(circle at 50% 25%, #ffffff 0%, var(--blue-pale) 70%); }
  .panel--back { left: 560px; background: linear-gradient(#ffffff 0%, #f5f9fd 100%); }
  .backdrop { position: absolute; inset: 0; }

  .brand { position: absolute; top: 198px; left: 0; width: 560px; text-align: center; }
  .brand__name { font-size: 32px; font-weight: 600; color: var(--ink-soft); letter-spacing: 0.5px; margin: 0; }
  .brand__tagline { margin: 10px 0 0; font-size: 11.5px; letter-spacing: 4.2px; color: var(--ink-soft); font-weight: 400; }

  .front-mark { position: absolute; top: 926px; width: 560px; text-align: center; margin: 0;
    color: var(--white); font-size: 34px; font-weight: 600; letter-spacing: 1px; }
  .front-web { position: absolute; top: 1078px; width: 560px; text-align: center; color: var(--white); font-size: 18px; font-weight: 300; }

  .services { position: absolute; top: 48px; width: 560px; text-align: center; margin: 0; font-size: 26px; font-weight: 300; color: var(--ink); }
  .photo { position: absolute; }
  .photo--kitchen { left: 24px; top: 132px; width: 242px; height: 364px;
    background: linear-gradient(172deg, #fbfbfa 0%, #eef0ee 35%, #e4e2dc 62%, #d9b994 82%, #c99a68 100%); }
  .photo--study { left: 293px; top: 132px; width: 242px; height: 364px;
    background: linear-gradient(175deg, #f3ebcc 0%, #ede2bd 45%, #e7dfc4 68%, #c9c5ae 85%, #a9a48e 100%); }
  .photo--bath { left: 24px; top: 573px; width: 511px; height: 342px;
    background: linear-gradient(160deg, #eed6c8 0%, #f3e1d6 40%, #3f9ea3 41%, #3f9ea3 46%, #efddd2 47%, #f6ebe4 75%, #d8c6bb 100%); }
  .reach { position: absolute; top: 520px; width: 560px; text-align: center; margin: 0; font-size: 22px; font-weight: 300; color: var(--ink); }
  .call { position: absolute; top: 942px; width: 560px; text-align: center; margin: 0; color: var(--ink-soft); font-size: 22px; font-weight: 300; line-height: 1.3; }
  .call__number { display: block; font-weight: 700; font-size: 22px; }
  .back-mark { position: absolute; top: 1085px; width: 560px; text-align: center; margin: 0;
    color: var(--white); font-size: 13px; font-weight: 600; letter-spacing: 0.5px; }
  .footer { position: absolute; bottom: 3px; left: 8px; right: 6px; display: flex; justify-content: space-between; color: var(--white); font-size: 19px; font-weight: 300; }
</style>
</head>
<body>
<main class="flyer">
  <section class="panel panel--front">
    <svg class="backdrop" width="560" height="1200" viewBox="0 0 560 1200" aria-hidden="true">
      <defs>
        <linearGradient id="front-side" x1="0" y1="0" x2="1" y2="1">
          <stop offset="0" stop-color="#a9c8ea"/>
          <stop offset="0.5" stop-color="#5f9bd5"/>
          <stop offset="1" stop-color="#4d8fcf"/>
        </linearGradient>
        <radialGradient id="front-base" cx="0.6" cy="0.75" r="0.8">
          <stop offset="0" stop-color="#5cb6e6"/>
          <stop offset="1" stop-color="#3b8ecf"/>
        </radialGradient>
      </defs>
      <polygon points="0,238 560,876 560,1200 0,1200" fill="url(#front-side)"/>
      <polygon points="381,670 560,570 560,876" fill="var(--blue-light)"/>
      <polygon points="0,892 381,670 560,876 560,1200 0,1200" fill="url(#front-base)"/>
    </svg>
    <div class="brand">
      <p class="brand__name">BRIGHTWELL-JOINERY</p>
      <p class="brand__tagline">CABINETRY SOLUTIONS FOR YOUR HOME</p>
    </div>
    <p class="front-mark">BRIGHTWELL-JOINERY</p>
    <div class="front-web">brightwell-joinery.com.au</div>
  </section>

  <section class="panel panel--back">
    <svg class="backdrop" width="560" height="1200" viewBox="0 0 560 1200" aria-hidden="true">
      <defs>
        <linearGradient id="back-band" x1="0" y1="0" x2="0" y2="1">
          <stop offset="0" stop-color="#7fb3e3"/>
          <stop offset="1" stop-color="#5b97d6"/>
        </linearGradient>
      </defs>
      <polygon points="0,956 210,1112 0,1200" fill="#c3dcf2"/>
      <polygon points="560,956 350,1112 560,1200" fill="#c3dcf2"/>
      <polygon points="0,1176 280,1018 560,1176 560,1200 0,1200" fill="url(#back-band)"/>
      <polygon points="280,1018 396,1094 280,1172 164,1094" fill="var(--blue-deep)"/>
    </svg>
    <h1 class="services">Kitchens I Benchtops I Custom Cabinetry</h1>
    <div class="photo photo--kitchen" role="img" aria-label="Photo of a white galley kitchen with timber floor"></div>
    <div class="photo photo--study" role="img" aria-label="Photo of a built-in study nook with desk and overhead cabinets"></div>
    <p class="reach">Servicing all areas, we come to you!</p>
    <div class="photo photo--bath" role="img" aria-label="Photo of a bathroom vanity with mirror cabinet and teal towels"></div>
    <p class="call">Call us now on <span class="call__number">0461 872 309</span></p>
    <p class="back-mark">BRIGHTWELL-JOINERY</p>
    <div class="footer">
      <span>enquiries@brightwell-joinery.com.au</span>
      <span>Lic. No. BLD 738402</span>
    </div>
  </section>
</main>
</body>
</html>
```